Tailbrook - eCommerce Design and Shopify Theme customisation

eCommerce Website Design - firstly with mockups then once we have chosen the design the successful designer will need to choose, purchase and customise a Shopify theme to match the design. We have a logo already designed and now want to create our web presence based on carrying up to 50 products on our website.
Target Market(s)
UK Pet Owners
Industry/Entity Type
Pet Shop
Requirements
Must have
- Design must be achievable using a customised Shopify theme - the successful designer will be responsible for the delivery of a working theme on our shopify website.
Should not have
- should not look cheap or have designs that aren't compatible or achievable with Shopify

```html
<!DOCTYPE html>
<html lang="en">
<head>
<meta charset="utf-8">
<title>Tailbrook – Pet Shop</title>
<link rel="stylesheet" href="https://fonts.googleapis.com/css2?family=Montserrat:wght@400;500;600;700&family=Open+Sans:wght@700&display=swap">
<style>
  :root {
    --frame: #e6e6e6;
    --white: #ffffff;
    --gold: #d6b53c;
    --ink: #2b2b2b;
    --muted: #555555;
    --section: #eeeeee;
    --price-red: #e3161b;
    --action-blue: #3798f5;
    --action-grey: #9b9b9b;
    --dark-button: #2d2410;
    --footer-bar: #f3f3f3;
  }
  * { box-sizing: border-box; margin: 0; padding: 0; }
  html, body { width: 796px; height: 1200px; overflow: hidden; }
  body {
    background: var(--frame);
    font-family: "Montserrat", Arial, sans-serif;
    color: var(--ink);
    position: relative;
  }
  .page { position: absolute; left: 9px; top: 9px; width: 778px; height: 1181px; background: var(--white); }

  /* Header */
  .site-header { position: absolute; left: 0; top: 0; width: 778px; height: 101px; }
  .brand { position: absolute; display: flex; align-items: center; gap: 8px; }
  .brand-dot { width: 18px; height: 18px; border-radius: 50%; background: var(--gold); }
  .brand-name { font-weight: 700; font-size: 22px; color: var(--ink); letter-spacing: -0.3px; }
  .site-header .brand { left: 19px; top: 37px; }
  .search { position: absolute; left: 468px; top: 39px; width: 208px; height: 28px; border: 1px solid #9a9a9a; border-radius: 4px; overflow: hidden; background: var(--white); }
  .search-label { position: absolute; left: 10px; top: 7px; font-size: 10px; font-weight: 500; color: #222; }
  .search-button { position: absolute; right: 0; top: 0; width: 31px; height: 26px; background: var(--gold); display: flex; align-items: center; justify-content: center; }
  .cart { position: absolute; left: 700px; top: 46px; display: flex; align-items: center; gap: 5px; font-size: 10px; font-weight: 500; color: #222; }

  /* Navigation */
  .main-nav { position: absolute; left: 0; top: 101px; width: 778px; height: 31px; background: var(--gold); }
  .nav-item { position: absolute; top: 10px; transform: translateX(-50%); font-size: 10.5px; font-weight: 700; color: var(--white); letter-spacing: 0.3px; white-space: nowrap; }

  /* Hero */
  .hero { position: absolute; left: 0; top: 132px; width: 778px; height: 306px;
    background: linear-gradient(135deg, #6d5f5f 0%, #8a7a78 45%, #cfc9c4 75%, #e9e6e2 100%); }
  .hero-arrow { position: absolute; top: 122px; width: 31px; height: 31px; background: var(--gold); display: flex; align-items: center; justify-content: center; opacity: 0.9; }
  .hero-arrow.prev { left: 0; }
  .hero-arrow.next { right: 0; }
  .hero-dots { position: absolute; left: 348px; top: 291px; display: flex; gap: 3px; }
  .hero-dots span { width: 18px; height: 3px; background: var(--white); }
  .hero-dots span.active { background: var(--gold); }

  /* Products */
  .products { position: absolute; left: 0; top: 438px; width: 778px; height: 462px; background: var(--section); }
  .section-title { position: absolute; left: 0; width: 778px; top: 62px; text-align: center; font-size: 18px; font-weight: 700; letter-spacing: 0.5px; color: #333; }
  .product-card { position: absolute; top: 110px; width: 196px; height: 303px; background: var(--white); }
  .product-name { position: absolute; left: 14px; top: 15px; font-size: 12px; font-weight: 500; color: #333; }
  .product-photo { position: absolute; left: 12px; top: 43px; width: 172px; height: 171px; }
  .price { position: absolute; left: 14px; top: 229px; display: flex; gap: 14px; font-size: 16.5px; font-weight: 500; }
  .price-was { position: relative; color: var(--muted); }
  .price-was::after { content: ""; position: absolute; left: -2px; right: -2px; top: 50%; height: 1.5px; background: var(--price-red); transform: rotate(-18deg); }
  .price-now { color: var(--price-red); font-weight: 600; }
  .card-actions { position: absolute; left: 12px; top: 266px; display: flex; gap: 6px; }
  .button-small { height: 21px; padding: 0 10px; border-radius: 2px; font-size: 10px; font-weight: 700; color: var(--white); display: flex; align-items: center; }
  .button-cart { background: var(--action-blue); }
  .button-more { background: var(--action-grey); }
  .carousel-arrow { position: absolute; top: 279px; }

  /* Mailing list */
  .mailing { position: absolute; left: 0; top: 900px; width: 778px; height: 107px; background: var(--gold); }
  .mailing-title { position: absolute; left: 41px; top: 41px; font-size: 18px; font-weight: 700; color: var(--white); }
  .email-field { position: absolute; left: 269px; top: 37px; width: 384px; height: 34px; background: var(--white); border-radius: 5px; padding: 9px 14px; font-size: 14px; color: #777; }
  .signup { position: absolute; left: 661px; top: 37px; width: 89px; height: 34px; background: var(--dark-button); border-radius: 5px; color: var(--white); font-size: 14px; font-weight: 700; display: flex; align-items: center; justify-content: center; letter-spacing: 0.3px; }

  /* Footer */
  .site-footer { position: absolute; left: 0; top: 1007px; width: 778px; height: 147px; }
  .site-footer .brand { left: 50%; top: 60px; transform: translateX(-50%); }
  .copyright { position: absolute; left: 0; top: 1154px; width: 778px; height: 27px; background: var(--footer-bar); text-align: center; font-family: "Open Sans", Arial, sans-serif; font-weight: 700; font-size: 7.5px; color: #333; padding-top: 9px; letter-spacing: 0.2px; }
</style>
</head>
<body>
<div class="page">

  <header class="site-header">
    <div class="brand"><span class="brand-dot"></span><span class="brand-name">Tailbrook</span></div>
    <div class="search">
      <span class="search-label">Search</span>
      <span class="search-button">
        <svg width="14" height="14" viewBox="0 0 14 14"><circle cx="6" cy="6" r="4.3" fill="none" stroke="#111" stroke-width="1.6"/><line x1="9.2" y1="9.2" x2="12.5" y2="12.5" stroke="#111" stroke-width="1.8" stroke-linecap="round"/></svg>
      </span>
    </div>
    <div class="cart">
      <svg width="15" height="12" viewBox="0 0 15 12"><path d="M0.5 1h2.2l2 7h7.3l1.8-5H3.6" fill="none" stroke="#222" stroke-width="1.1"/><circle cx="5.5" cy="10.5" r="1" fill="#222"/><circle cx="11" cy="10.5" r="1" fill="#222"/></svg>
      <span>Cart (0)</span>
    </div>
  </header>

  <nav class="main-nav">
    <span class="nav-item" style="left:171px">HOME</span>
    <span class="nav-item" style="left:267px">PRODUCTS</span>
    <span class="nav-item" style="left:374px">SPECIALS</span>
    <span class="nav-item" style="left:478px">ABOUT US</span>
    <span class="nav-item" style="left:588px">CONTACT US</span>
  </nav>

  <section class="hero" role="img" aria-label="Black and white French bulldog sniffing a bowl of biscuits on a table">
    <span class="hero-arrow prev"><svg width="10" height="14" viewBox="0 0 10 14"><path d="M7.5 1.5L2.5 7l5 5.5" fill="none" stroke="#fff" stroke-width="2"/></svg></span>
    <span class="hero-arrow next"><svg width="10" height="14" viewBox="0 0 10 14"><path d="M2.5 1.5L7.5 7l-5 5.5" fill="none" stroke="#fff" stroke-width="2"/></svg></span>
    <div class="hero-dots"><span class="active"></span><span></span><span></span><span></span></div>
  </section>

  <section class="products">
    <h2 class="section-title">OUR PRODUCTS</h2>

    <svg class="carousel-arrow" style="left:43px" width="18" height="26" viewBox="0 0 18 26"><path d="M14 3L5 13l9 10" fill="none" stroke="#8c8c8c" stroke-width="4"/></svg>

    <article class="product-card" style="left:80px">
      <h3 class="product-name">Orthopaedic Dog Beds</h3>
      <div class="product-photo" role="img" aria-label="Cat stretched out asleep on a soft blanket" style="background:linear-gradient(160deg,#3a3a32 0%,#b9a48f 45%,#efe6dc 100%)"></div>
      <div class="price"><span class="price-was">$25.99</span><span class="price-now">$19.99</span></div>
      <div class="card-actions"><span class="button-small button-cart">Add to Cart</span><span class="button-small button-more">Learn More</span></div>
    </article>

    <article class="product-card" style="left:291px">
      <h3 class="product-name">Orthopaedic Dog Beds</h3>
      <div class="product-photo" role="img" aria-label="Pug wrapped in a beige blanket on a bed" style="background:linear-gradient(170deg,#6f6a6e 0%,#9c8479 45%,#d9d2d0 100%)"></div>
      <div class="price"><span class="price-was">$13.99</span><span class="price-now">$10.99</span></div>
      <div class="card-actions"><span class="button-small button-cart">Add to Cart</span><span class="button-small button-more">Learn More</span></div>
    </article>

    <article class="product-card" style="left:502px">
      <h3 class="product-name">Orthopaedic Dog Beds</h3>
      <div class="product-photo" role="img" aria-label="Puppy sitting in a red polka-dot cup on grass" style="background:linear-gradient(180deg,#c9d1c0 0%,#e7dcd6 40%,#d9504a 70%,#5f8f3e 100%)"></div>
      <div class="price"><span class="price-was">$38.99</span><span class="price-now">$33.99</span></div>
      <div class="card-actions"><span class="button-small button-cart">Add to Cart</span><span class="button-small button-more">Learn More</span></div>
    </article>

    <svg class="carousel-arrow" style="left:716px" width="18" height="26" viewBox="0 0 18 26"><path d="M4 3l9 10-9 10" fill="none" stroke="#8c8c8c" stroke-width="4"/></svg>
  </section>

  <section class="mailing">
    <h2 class="mailing-title">Join Our Mailing List</h2>
    <div class="email-field">Email Address</div>
    <div class="signup">SIGN UP</div>
  </section>

  <footer class="site-footer">
    <div class="brand"><span class="brand-dot"></span><span class="brand-name">Tailbrook</span></div>
  </footer>
  <div class="copyright">COPYRIGHT © 2019 TAILBROOK. ALL RIGHTS RESERVED.</div>

</div>
</body>
</html>
```